refurbishment of diamond cut alloy wheels

we need to design a flyer that will catch the eye of the customer to refurbish diamond cut alloy wheels. we refurbish the wheels by using the latest CNC machine to precision cut and resurface the wheel. we would like before and after pictures of maybe Kelvaron, DXT, Orsa wheels to give it a prestige look. The final design should communicate an expensive look and providing a good image for the business. The colours that I would like to use is black and red which should make the flyer stand out. The logo must sit on a black background without the wordings of specialists in HJ, Orsa etc and also without servicing, diagnostics etc as well. This flyer is just to communicate refurbishment of alloy wheels to high standard.

Target Market(s)

any members of the public and car dealerships

Industry/Entity Type

Automotive

Colors

Designer to choose colors to be used in the design.

Requirements
Must have
• Wow factor with great images of wheels
Nice to have
• Maybe on the front of the flyer it has a picture of a wheel and then on the back of the flyer it has before and after pictures to show how just how incredible it is to refurbish wheels
Should not have
• other makes of wheels apart from DXT, Orsa, and any other high end makes of vehicles wheels

```html
<!DOCTYPE html>
<html lang="en">
<head>
<meta charset="utf-8">
<title>Kestrel Motors – Diamond Cut Alloy Wheel Flyer</title>
<link rel="stylesheet" href="https://fonts.googleapis.com/css2?family=Montserrat:wght@400;600;700;800&family=Quicksand:wght@400;500;600&display=swap">
<style>
  :root {
    --stage: #c9c9cb;
    --page: #0b0b0d;
    --page-deep: #000000;
    --ink: #ffffff;
    --ink-soft: #cfcfd4;
    --ink-dim: #9a9aa2;
    --red: #d61f26;
    --red-dark: #8e0f14;
    --frame: #8a8a92;
    --rule: #d8d8dc;
  }
  * { box-sizing: border-box; margin: 0; padding: 0; }
  html, body { width: 945px; height: 1200px; overflow: hidden; }
  body {
    background: var(--stage);
    font-family: "Quicksand", "Century Gothic", sans-serif;
    color: var(--ink);
    position: relative;
  }
  .page {
    position: absolute;
    top: 258px;
    width: 452px;
    height: 684px;
    background: radial-gradient(ellipse at 60% 35%, #1d1d22 0%, var(--page) 55%, var(--page-deep) 100%);
    overflow: hidden;
  }
  .page--front { left: 12px; }
  .page--back  { left: 481px; }

  /* Front */
  .hero-wheel {
    position: absolute;
    left: 150px; top: 0; width: 302px; height: 600px;
    background: radial-gradient(circle at 70% 42%, #5b5c62 0%, #34353a 22%, #1a1a1e 45%, rgba(10,10,12,0) 72%);
  }
  .headline {
    position: absolute; left: 36px; top: 50px;
    font-family: "Montserrat", Arial, sans-serif;
    font-weight: 800; font-size: 31px; line-height: 37px;
    letter-spacing: 0.5px; text-transform: uppercase;
    color: #f2f2f2;
  }
  .headline-bar {
    position: absolute; left: 36px; top: 175px; width: 210px; height: 6px;
    background: linear-gradient(90deg, #e8e8ea, rgba(200,200,205,0));
  }
  .brand {
    position: absolute; left: 40px; top: 222px;
    display: flex; align-items: center; gap: 10px;
  }
  .brand-mark { width: 26px; height: 26px; background: var(--red); }
  .brand-name {
    font-family: "Montserrat", Arial, sans-serif;
    font-weight: 800; font-size: 22px; text-transform: uppercase; color: var(--ink);
  }
  .intro-box {
    position: absolute; left: 40px; top: 264px; width: 236px; height: 272px;
    border: 1.5px solid var(--frame); border-radius: 10px;
    background: rgba(10,10,12,0.6);
    padding: 14px 12px 10px 12px;
  }
  .intro-lead { font-size: 15.5px; line-height: 19px; font-weight: 500; margin-bottom: 14px; }
  .intro-copy { font-size: 7.6px; line-height: 10px; color: var(--ink-soft); margin-bottom: 10px; }
  .front-cta {
    position: absolute; left: 36px; top: 594px; width: 200px;
    font-size: 11.5px; line-height: 15px; color: var(--ink-soft);
  }

  .phone-button {
    position: absolute;
    width: 178px; height: 40px;
    border-radius: 8px;
    background: linear-gradient(180deg, #ef3a40 0%, var(--red) 50%, var(--red-dark) 100%);
    display: flex; align-items: center; justify-content: center; gap: 8px;
    font-family: "Montserrat", Arial, sans-serif;
    font-weight: 600; font-size: 17px; color: var(--ink);
  }
  .phone-button svg { width: 16px; height: 16px; fill: var(--ink); }
  .page--front .phone-button { left: 250px; top: 590px; }
  .page--back .phone-button  { left: 250px; top: 578px; }

  /* Back */
  .back-title {
    position: absolute; left: 0; right: 0; top: 26px; text-align: center;
    font-family: "Montserrat", Arial, sans-serif; font-weight: 700; font-size: 14px;
  }
  .compare { position: absolute; top: 69px; width: 190px; height: 226px; }
  .compare--before { left: 28px; }
  .compare--after  { left: 231px; }
  .compare-photo { width: 100%; height: 100%; }
  .compare--before .compare-photo { background: radial-gradient(circle at 50% 45%, #e4e4e6 0%, #a9a9ad 40%, #5a5a5f 75%, #2c2c30 100%); }
  .compare--after .compare-photo  { background: radial-gradient(circle at 50% 45%, #d8d9dc 0%, #6f7075 35%, #1c1c20 70%, #0d0d10 100%); }
  .compare-tag {
    position: absolute; left: 38px; bottom: -8px; width: 114px; height: 30px;
    border-radius: 6px;
    background: linear-gradient(180deg, #ef3a40 0%, var(--red) 50%, var(--red-dark) 100%);
    text-align: center; line-height: 30px;
    font-family: "Montserrat", Arial, sans-serif; font-weight: 600; font-size: 14px;
  }
  .service-area {
    position: absolute; left: 30px; right: 30px; top: 334px; text-align: center;
    font-size: 11.4px; line-height: 16px; font-weight: 500;
  }
  .service-copy {
    position: absolute; left: 32px; right: 32px; top: 404px; text-align: center;
    font-size: 7.4px; line-height: 10px; color: var(--ink-soft);
  }
  .back-rule { position: absolute; left: 28px; right: 28px; top: 544px; height: 2px; background: var(--rule); }
  .back-cta { position: absolute; left: 28px; top: 562px; }
  .back-cta-small { font-size: 10px; letter-spacing: 0.5px; color: var(--ink-soft); text-transform: uppercase; }
  .back-cta-large { font-size: 19px; letter-spacing: 0.5px; text-transform: uppercase; margin-top: 2px; }
</style>
</head>
<body>

<section class="page page--front">
  <div class="hero-wheel" role="img" aria-label="Close-up of a dark diamond cut multi-spoke alloy wheel"></div>
  <h1 class="headline">Refurbish<br>Diamond Cut<br>Alloy Wheels</h1>
  <div class="headline-bar"></div>
  <div class="brand">
    <span class="brand-mark"></span>
    <span class="brand-name">Kestrel Motors</span>
  </div>
  <div class="intro-box">
    <p class="intro-lead">We refurbish the wheels by using the latest CNC machine to precision cut and resurface the wheel.</p>
    <p class="intro-copy">If you are looking to refresh the look of your car but don't want the expense of new alloys, with a wide range of limited edition colours to choose from why not consider customising and refurbishing your existing alloys?</p>
    <p class="intro-copy">If you've had your alloy wheels long enough for them to require alloy refurbishment you can choose from a wide range of colours for refurbishment or choose a brand new set from our comprehensive range. At Apex Wheels &amp; Tyres, we stock an extensive range of the latest designs from all the leading suppliers and manufacturers so you are sure to find a stylish new design.</p>
  </div>
  <p class="front-cta">If you need premier Alloy Refurbishment services in Slough, please contact us:</p>
  <div class="phone-button">
    <svg viewBox="0 0 24 24" aria-hidden="true"><path d="M6.6 10.8a15.1 15.1 0 0 0 6.6 6.6l2.2-2.2a1 1 0 0 1 1-.25 11.4 11.4 0 0 0 3.6.57 1 1 0 0 1 1 1V20a1 1 0 0 1-1 1A17 17 0 0 1 3 4a1 1 0 0 1 1-1h3.5a1 1 0 0 1 1 1c0 1.25.2 2.45.57 3.6a1 1 0 0 1-.25 1z"/></svg>
    <span>01632 960 418</span>
  </div>
</section>

<section class="page page--back">
  <h2 class="back-title">Alloy Refurbishment Specialists in and around Slough</h2>
  <figure class="compare compare--before">
    <div class="compare-photo" role="img" aria-label="Worn silver multi-spoke alloy wheel before refurbishment"></div>
    <figcaption class="compare-tag">Before</figcaption>
  </figure>
  <figure class="compare compare--after">
    <div class="compare-photo" role="img" aria-label="Black and polished five-spoke alloy wheel after diamond cut refurbishment"></div>
    <figcaption class="compare-tag">After</figcaption>
  </figure>
  <p class="service-area">We cater to all locations in and around Colnbrook, Windsor, Hayes, Hounslow, Staines, Ascot and Ashford. For all car body modifications and restorations get in touch with our team of experts today!</p>
  <p class="service-copy">Every wheel is inspected, cleaned and stripped before repair. Kerb damage, corrosion and buckles are corrected by hand, then the face is cut on our CNC lathe for a precise factory finish. A durable lacquer seals the surface against salt, grime and brake dust. Most sets are returned within a day, balanced and ready to fit, with a clear quote agreed before any work begins on your car.</p>
  <div class="back-rule"></div>
  <div class="back-cta">
    <p class="back-cta-small">If your alloys need refurbishment</p>
    <p class="back-cta-large">Contact us today</p>
  </div>
  <div class="phone-button">
    <svg viewBox="0 0 24 24" aria-hidden="true"><path d="M6.6 10.8a15.1 15.1 0 0 0 6.6 6.6l2.2-2.2a1 1 0 0 1 1-.25 11.4 11.4 0 0 0 3.6.57 1 1 0 0 1 1 1V20a1 1 0 0 1-1 1A17 17 0 0 1 3 4a1 1 0 0 1 1-1h3.5a1 1 0 0 1 1 1c0 1.25.2 2.45.57 3.6a1 1 0 0 1-.25 1z"/></svg>
    <span>01632 960 418</span>
  </div>
</section>

</body>
</html>
```